Halloween Style Website Design

We need a website design with a Halloween theme.

I have provided 3 wireframes to work from. If you like you can just design the homepage first. If we like your designs we will instruct you to design the other pages once we narrow them down.

The website will be totally halloween themed. We will use vector type designs.

We want a feel similar to this style I guess:

https://v.clipvarn.net/pic/Kt7mQ2wLx9aR/largestill.jpg
https://media.sketchlorn.com/members/5172804/captures/3318467/panel_2__2_.jpg
https://img4.plotmerrow.com/p/1000x1000/41/09/halloween-castle-background-design-vector-58301746.jpg
https://pix.graventa.com/free-vector/decorative-halloween-background-flat-style_48-7715302946.jpg?size=626&ext=jpg
https://bx7.quillomedia.net/jpg/05/31/96/48/500_K_531964827_rTmWbZeLoNcYpQ4sVhGaJdKiUvXyFe2s.jpg

```html
<!DOCTYPE html>
<html lang="en">
<head>
<meta charset="utf-8">
<title>Trick or Treet – Halloween</title>
<link rel="stylesheet" href="https://fonts.googleapis.com/css2?family=Roboto:wght@400;700&family=Montserrat:wght@500;600;700&family=Mystery+Quest&display=swap">
<style>
:root{
  --orange:#f7931e;
  --night:#120d12;
  --teal:#1fb5a4;
  --white:#ffffff;
  --grey-text:#8a8a8a;
  --ink:#1a1a1a;
}
*{margin:0;padding:0;box-sizing:border-box}
html,body{width:822px;height:1200px;overflow:hidden;background:var(--white);font-family:'Roboto',sans-serif}
.page{position:relative;width:822px;height:1200px;overflow:hidden}
.abs{position:absolute}

.hero{left:0;top:0;width:822px;height:372px;
  background:radial-gradient(circle at 430px 150px,#d9832a 0,#c4661a 110px,#9a4310 230px,#3a1a08 360px,#0d0704 470px)}
.hero-divider{left:0;top:377px;width:822px;height:3px;background:var(--night)}
.brand{left:124px;top:18px;width:98px;text-align:center;color:var(--white);font-weight:400;font-size:17px;letter-spacing:1px}
.nav{left:302px;top:28px;display:flex;gap:13px}
.nav a{color:var(--white);font-family:'Montserrat',sans-serif;font-weight:600;font-size:10px;text-decoration:none}
.login{left:529px;top:26px;color:var(--white);font-family:'Montserrat',sans-serif;font-weight:500;font-size:11px}
.btn-signup{left:576px;top:19px;width:68px;height:24px;background:var(--orange);color:var(--white);font-family:'Montserrat',sans-serif;font-weight:600;font-size:8.5px;display:flex;align-items:center;justify-content:center}
.hero-rule{left:107px;top:73px;width:608px;height:1px;background:var(--white)}
.hero-title{left:106px;top:100px;color:var(--white);font-family:'Mystery Quest',cursive;font-weight:400;font-size:31px;letter-spacing:1px;white-space:nowrap}
.hero-copy{left:107px;top:168px;width:490px;color:var(--white);font-size:8.4px;line-height:15px}
.btn-learn{left:105px;top:245px;width:87px;height:22px;border:2px solid var(--orange);color:var(--white);font-weight:700;font-size:11px;display:flex;align-items:center;justify-content:center}
.social{left:791px;top:133px;display:flex;flex-direction:column;gap:17px}
.social span{width:11px;height:11px;border-radius:50%;background:var(--white)}
.chevron{width:9px;height:6px}

.card{top:442px;height:215px;border-radius:3px;overflow:hidden}
.card-build{left:60px;width:229px;background:linear-gradient(180deg,#a84a12 0,#6a2c0e 45%,#1e1010 100%)}
.card-tricks{left:296px;width:229px;background:linear-gradient(180deg,#1f3a3c 0,#173032 50%,#0e1c1e 100%)}
.card-treets{left:532px;width:222px;background:linear-gradient(180deg,#1a1c26 0,#2a2018 60%,#3a2612 100%)}
.card-title{position:absolute;left:0;right:0;top:12px;text-align:center;color:var(--orange);font-family:'Mystery Quest',cursive;font-weight:400;font-size:38px}
.card-copy{position:absolute;left:27px;right:12px;top:68px;color:var(--white);font-size:8.4px;line-height:15px}
.card-btn{position:absolute;bottom:0;width:81px;height:17px;border-radius:6px 6px 0 0;background:var(--teal);color:var(--white);font-size:7.5px;font-weight:700;text-align:center;padding-top:5px}
.to-top{left:786px;width:24px;height:24px;background:#b8b8b8;display:flex;align-items:center;justify-content:center}

.promo-art{left:54px;top:690px;width:238px;height:138px;background:radial-gradient(circle at 120px 60px,#c2611a 0,#5a2a0c 60px,#141010 130px)}
.promo-copy{left:314px;top:690px;width:290px;color:var(--grey-text);font-size:9.7px;line-height:18px}
.promo-copy b,.hero-copy b,.card-copy b{font-weight:700}
.promo-cta{left:635px;top:744px;color:var(--teal);font-family:'Montserrat',sans-serif;font-weight:600;font-size:16.5px}

.greeting{left:0;top:860px;width:822px;height:266px;background:radial-gradient(ellipse at 230px 110px,#5a1a0c 0,#2a0e0a 110px,transparent 200px),radial-gradient(ellipse at 430px 110px,#6a2410 0,#2a0e0a 120px,transparent 210px),linear-gradient(180deg,#0d0d14 0,#140c0c 60%,#1c100a 100%)}
.greeting-title{left:67px;top:908px;color:var(--white);font-family:'Mystery Quest',cursive;font-weight:400;font-size:29px;letter-spacing:2px}
.greeting-copy{left:67px;top:955px;width:685px;color:var(--white);font-size:8.4px;line-height:15px}
.btn-connect{left:67px;top:1040px;width:104px;height:24px;border-radius:3px;background:var(--teal);color:var(--white);font-weight:700;font-size:9px;display:flex;align-items:center;justify-content:center}

.footer-rule{left:161px;top:1141px;width:499px;height:1px;background:var(--ink)}
.footer-nav{left:0;top:1158px;width:822px;display:flex;justify-content:center;gap:12px}
.footer-nav a{color:var(--ink);font-family:'Montserrat',sans-serif;font-weight:600;font-size:14.5px;text-decoration:none}
.copyright{left:0;top:1180px;width:822px;text-align:center;color:var(--ink);font-size:11.5px}
</style>
</head>
<body>
<div class="page">

  <div class="abs hero" role="img" aria-label="Orange moonlit Halloween night with bats, cobwebs and carved pumpkins"></div>
  <div class="abs hero-divider"></div>
  <div class="abs brand">HALLOWEEN</div>
  <nav class="abs nav"><a>Home</a><a>Build</a><a>Tricks</a><a>Treets</a></nav>
  <div class="abs login">Login</div>
  <div class="abs btn-signup">Sign Up</div>
  <div class="abs hero-rule"></div>
  <h1 class="abs hero-title">Welcome To My Trick Or Treet!</h1>
  <p class="abs hero-copy"><b>Lorem Ipsum</b> is simply dummy text of the printing and typesetting industry. Lorem Ipsum has been the industry's standard dummy text ever since the 1500s, when an unknown printer took a galley of type and scrambled it to make a type specimen book. It has survived not only five centuries, but also the leap into electronic typesetting, remaining essentially unchanged. It was popularised in the 1960s with the release of Vellmark sheets containing Lorem Ipsum passages,</p>
  <div class="abs btn-learn">LEARN MORE</div>
  <div class="abs social"><span></span><span></span><span></span><span></span></div>
  <svg class="abs chevron" style="left:794px;top:352px" viewBox="0 0 10 6"><path d="M1 5 L5 1 L9 5" stroke="#fff" stroke-width="2" fill="none"/></svg>

  <div class="abs card card-build" role="img" aria-label="Haunted tree and cobweb scene in orange">
    <div class="card-title">BUILD</div>
    <p class="card-copy"><b>Lorem Ipsum</b> is simply dummy text of the printing and typesetting industry. Lorem Ipsum has been the industry's standard dummy text ever since the 1500s, when an unknown printer took a galley of type and scrambled it to make a type specimen book. It has survived not only five centuries, but also the leap into electronic typesetting, remaining essentially unchanged.</p>
    <div class="card-btn" style="left:74px">Read More</div>
  </div>
  <div class="abs card card-tricks" role="img" aria-label="Moonlit graveyard scene in teal">
    <div class="card-title">TRICKS</div>
    <p class="card-copy"><b>Lorem Ipsum</b> is simply dummy text of the printing and typesetting industry. Lorem Ipsum has been the industry's standard dummy text ever since the 1500s, when an unknown printer took a galley of type and scrambled it to make a type specimen book. It has survived not only five centuries, but also the leap into electronic typesetting, remaining essentially unchanged.</p>
    <div class="card-btn" style="left:74px">Read More</div>
  </div>
  <div class="abs card card-treets" role="img" aria-label="Dark candlelit scene with an open book">
    <div class="card-title">TREETS</div>
    <p class="card-copy"><b>Lorem Ipsum</b> is simply dummy text of the printing and typesetting industry. Lorem Ipsum has been the industry's standard dummy text ever since the 1500s, when an unknown printer took a galley of type and scrambled it to make a type specimen book. It has survived not only five centuries, but also the leap into electronic typesetting, remaining essentially unchanged.</p>
    <div class="card-btn" style="left:71px">Read More</div>
  </div>
  <div class="abs to-top" style="top:618px"><svg class="chevron" viewBox="0 0 10 6"><path d="M1 5 L5 1 L9 5" stroke="#fff" stroke-width="2" fill="none"/></svg></div>

  <div class="abs promo-art" role="img" aria-label="Glowing pumpkins on a dark background with the Halloween title"></div>
  <p class="abs promo-copy"><b>Lorem Ipsum</b> is simply dummy text of the printing and typesetting industry. Lorem Ipsum has been the industry's standard dummy text ever since the 1500s, when an unknown printer took a galley of type and scrambled it to make a type specimen book. It has survived not only five centuries, but also the leap into electronic typesetting, remaining essentially unchanged.</p>
  <div class="abs promo-cta">Sign Up Now</div>

  <div class="abs greeting" role="img" aria-label="Dark night scene lit by glowing carved pumpkins"></div>
  <svg class="abs chevron" style="left:794px;top:903px" viewBox="0 0 10 6"><path d="M1 5 L5 1 L9 5" stroke="#fff" stroke-width="2" fill="none"/></svg>
  <h2 class="abs greeting-title">HAPPY HALLOWEEN</h2>
  <p class="abs greeting-copy">Lorem ipsum dolor sit amet, consectetur adipiscing elit. Ut elit tellus, luctus nec ullamcorper mattis, pulvinar dapibus leo.It is a long established fact that a reader will be distracted by the readable content of a page when looking at its layout. The point of using Lorem Ipsum is that it has a more-or-less normal distribution of letters, as opposed to using 'Content here, content here', making it look like readable English. Many desktop publishing packages and web page editors now use Lorem Ipsum as their default model text, and a search for 'lorem ipsum' will uncover many web sites still in their infancy.</p>
  <div class="abs btn-connect">LET'S CONNECT</div>

  <div class="abs footer-rule"></div>
  <nav class="abs footer-nav"><a>Home</a><a>build</a><a>Tricks</a><a>Treets</a></nav>
  <div class="abs copyright">Copyright @ 2020 - my trick or treet - <u>privacy poolicy</u></div>
  <div class="abs to-top" style="top:1171px"><svg class="chevron" viewBox="0 0 10 6"><path d="M1 5 L5 1 L9 5" stroke="#fff" stroke-width="2" fill="none"/></svg></div>

</div>
</body>
</html>
```